Modern looking signage for dental office.

Exterior signage for passing cars
Target Market(s)
Cars passing by
Font styles to use
Sans Serif
Colors
3276b5
Requirements
Must have
- Logo
- OPEN ON SUTURDAY AND SUNDAY
- NIGHT CLINIC AVAILABLE
- PLEASE USE THE FONT TYPE IN FILE 4 UPLOADED BELOW.
- (482) 730-2964
- Modern looking

```html
<!DOCTYPE html>
<html lang="en">
<head>
<meta charset="UTF-8">
<title>Harbor Dental – Weekend &amp; Night Clinic Sign</title>
<link rel="stylesheet" href="https://fonts.googleapis.com/css2?family=Open+Sans:wdth,wght@75..100,300..800&display=swap">
<style>
  :root {
    --ink: #2f2f33;
    --blue-light: #3a8df0;
    --blue: #2a74e2;
    --blue-deep: #1a52c4;
    --white: #ffffff;
    --silver-light: #f4f6f7;
    --silver: #c9d0d3;
    --silver-dark: #8e989c;
    --phone-blue: #2b72e0;
  }
  * { margin: 0; padding: 0; box-sizing: border-box; }
  html, body {
    width: 1200px; height: 1000px; overflow: hidden;
    background: var(--white);
  }
  .sign {
    position: relative;
    width: 1200px; height: 1000px;
    overflow: hidden;
    font-family: "Open Sans", Arial, sans-serif;
    background: radial-gradient(ellipse at 20% 20%, #ffffff 0%, #f1f3f4 60%, #e6e9ea 100%);
  }
  .sign__art { position: absolute; inset: 0; }

  .brand-mark {
    position: absolute;
    left: 48px; top: 32px;
    width: 236px; height: 236px;
    border: 3px solid var(--ink);
    border-radius: 50%;
    background: var(--white);
  }
  .brand {
    position: absolute;
    left: 0; top: 0;
    width: 1200px; height: 320px;
  }
  .brand__name {
    font-family: "Open Sans", Arial, sans-serif;
    font-size: 148px;
    font-weight: 400;
    font-stretch: 75%;
    font-variation-settings: "wdth" 75;
    fill: var(--ink);
  }
  .brand__tagline {
    font-family: "Open Sans", Arial, sans-serif;
    font-size: 52px;
    font-weight: 400;
    font-stretch: 75%;
    font-variation-settings: "wdth" 75;
    fill: var(--ink);
  }

  .hours {
    position: absolute;
    left: 0; width: 1200px;
    text-align: center;
    color: var(--white);
    font-weight: 700;
    line-height: 1;
    white-space: nowrap;
    text-shadow: 0 3px 6px rgba(10, 40, 120, 0.45);
  }
  .hours--open { top: 430px; font-size: 60px; }
  .hours--days { top: 498px; font-size: 102px; letter-spacing: -1px; }
  .hours--days .hours__and { font-size: 52px; vertical-align: 18px; margin: 0 24px; }
  .hours--night { top: 604px; font-size: 78px; letter-spacing: -2px; }

  .phone {
    position: absolute;
    left: 180px; top: 780px;
    width: 860px; height: 120px;
    display: flex; align-items: center; justify-content: center; gap: 26px;
  }
  .phone__icon { width: 96px; height: 96px; flex: none; }
  .phone__number {
    font-size: 104px;
    font-weight: 800;
    line-height: 1;
    letter-spacing: -1px;
    color: var(--phone-blue);
    white-space: nowrap;
    text-shadow: 0 0 2px #fff, 0 0 4px #fff, 0 3px 6px rgba(0, 0, 0, 0.25);
  }
</style>
</head>
<body>
<main class="sign">
  <svg class="sign__art" width="1200" height="1000" viewBox="0 0 1200 1000" aria-hidden="true">
    <defs>
      <linearGradient id="bandBlue" x1="0" y1="0" x2="0" y2="1">
        <stop offset="0" stop-color="var(--blue-light)"/>
        <stop offset="0.55" stop-color="var(--blue)"/>
        <stop offset="1" stop-color="var(--blue-deep)"/>
      </linearGradient>
      <linearGradient id="silverEdge" x1="0" y1="0" x2="1" y2="0">
        <stop offset="0" stop-color="var(--silver)"/>
        <stop offset="0.5" stop-color="var(--silver-light)"/>
        <stop offset="1" stop-color="var(--silver-dark)"/>
      </linearGradient>
      <linearGradient id="plateFill" x1="0" y1="0" x2="0" y2="1">
        <stop offset="0" stop-color="#ffffff"/>
        <stop offset="0.55" stop-color="#f1f3f4"/>
        <stop offset="1" stop-color="#c7cdd0"/>
      </linearGradient>
    </defs>

    <path class="band-rim" d="M0 368 Q600 318 1200 362 L1200 1000 L0 1000 Z" fill="url(#silverEdge)"/>
    <path class="band" d="M0 382 Q600 340 1200 378 L1200 948 Q600 918 0 948 Z" fill="url(#bandBlue)"/>

    <line x1="52" y1="462" x2="440" y2="458" stroke="#ffffff" stroke-width="3"/>
    <line x1="760" y1="458" x2="1150" y2="462" stroke="#ffffff" stroke-width="3"/>

    <polygon points="128,738 1072,738 1150,842 1072,946 128,946 50,842"
             fill="url(#plateFill)" stroke="var(--silver-dark)" stroke-width="4"/>
    <polygon points="136,748 1064,748 1138,842 1064,936 136,936 62,842"
             fill="none" stroke="#ffffff" stroke-width="3" opacity="0.8"/>
  </svg>

  <div class="brand-mark" aria-hidden="true"></div>
  <svg class="brand" width="1200" height="320" viewBox="0 0 1200 320" role="group" aria-label="Harbor Dental, Modern General Dentistry">
    <text class="brand__name" x="312" y="212" textLength="842" lengthAdjust="spacingAndGlyphs">HARBOR DENTAL</text>
    <text class="brand__tagline" x="392" y="287" textLength="650" lengthAdjust="spacingAndGlyphs">MODERN GENERAL DENTISTRY</text>
  </svg>

  <p class="hours hours--open">OPEN ON</p>
  <p class="hours hours--days">SATURDAY<span class="hours__and">AND</span>SUNDAY</p>
  <p class="hours hours--night">NIGHT CLINIC AVAILABLE</p>

  <div class="phone">
    <svg class="phone__icon" viewBox="0 0 96 96" aria-hidden="true">
      <path d="M30 22 L38 38 Q40 42 36 45 L32 48 Q38 62 50 70 L54 66 Q57 63 61 65 L76 73 Q79 75 77 79 L73 86 Q70 90 64 89 Q34 82 16 48 Q11 38 16 30 L22 24 Q26 20 30 22 Z"
            fill="none" stroke="var(--phone-blue)" stroke-width="6" stroke-linejoin="round"/>
      <path d="M52 34 Q62 36 64 46" fill="none" stroke="var(--phone-blue)" stroke-width="6" stroke-linecap="round"/>
      <path d="M54 20 Q74 24 78 44" fill="none" stroke="var(--phone-blue)" stroke-width="6" stroke-linecap="round"/>
    </svg>
    <span class="phone__number">(482) 730-2964</span>
  </div>
</main>
</body>
</html>
```